Business card design needed

I need a business card for my new business.
I make environmentally friendly candles from all natural premium ingredients.
The candles are hand-poured locally in Melbourne, Australia.
I also want my card to match my website www.velmirawicks.com.au (similar colours, font). Can add additional fonts to create more interest...
I want my design to reflect class and simplicity.
Target Market(s)
Target audience 25-50
The candles represent luxury but need to appeal to the environmentally conscious...
Needs to appeal to both men and women. A luxury gift a man would buy for his girlfriend or mother or for his home and for a woman it needs to represent quality...
Industry/Entity Type
Business
Contact Information for Business Card
Velmira Candles
Hand-Poured Eco Soy Candles
Lorraine Quibell - Founder
0438 276 904
www.velmirawicks.com.au
Logo Text
VELMIRA
Logo styles of interest
Wordmark Logo
Look and feel
Each slider illustrates characteristics of the customer's brand and the style your logo design should communicate.

```html
<!DOCTYPE html>
<html lang="en">
<head>
<meta charset="utf-8">
<title>Velmira Candles – Business Card</title>
<link rel="stylesheet" href="https://fonts.googleapis.com/css2?family=Rokkitt:ital,wght@0,300;0,400;0,700;1,300&display=swap">
<style>
  :root {
    --backdrop: #d9d6d1;
    --card-light: #f1f1ef;
    --card-dark: #3b3c3d;
    --ink-dark: #3a3a3a;
    --ink-muted: #6e6e6e;
    --ink-light: #c9c9c9;
    --ink-light-muted: #a9a9a9;
  }
  * { margin: 0; padding: 0; box-sizing: border-box; }
  html, body {
    width: 1200px;
    height: 720px;
    overflow: hidden;
    background: var(--backdrop);
    font-family: "Rokkitt", "Rockwell", serif;
  }
  .stage {
    width: 1200px;
    height: 720px;
    display: flex;
    align-items: center;
    justify-content: center;
    gap: 60px;
  }
  .card {
    width: 500px;
    height: 286px;
    display: flex;
    flex-direction: column;
    align-items: center;
    text-align: center;
    box-shadow: 0 2px 10px rgba(0, 0, 0, 0.12);
  }
  .card--front {
    background: var(--card-light);
    color: var(--ink-dark);
    padding-top: 40px;
  }
  .card--back {
    background: var(--card-dark);
    color: var(--ink-light);
    justify-content: center;
    padding-bottom: 6px;
  }
  .wordmark {
    font-weight: 300;
    font-size: 38px;
    letter-spacing: 2px;
    line-height: 1;
  }
  .rule {
    width: 96px;
    height: 1px;
    margin: 10px 0 9px;
    background: currentColor;
  }
  .tagline {
    font-style: italic;
    font-weight: 300;
    font-size: 14px;
    letter-spacing: 0.5px;
  }
  .card--front .tagline { color: var(--ink-muted); }
  .card--back .tagline { color: var(--ink-light-muted); }
  .person {
    margin-top: 26px;
  }
  .person__name {
    font-weight: 700;
    font-size: 22px;
    letter-spacing: 1px;
    line-height: 1;
  }
  .person__role {
    font-weight: 400;
    font-size: 16px;
    letter-spacing: 0.5px;
    margin-top: 3px;
  }
  .contact {
    margin-top: 24px;
    font-weight: 400;
    font-size: 17px;
    letter-spacing: 0.8px;
    line-height: 1.4;
  }
</style>
</head>
<body>
  <main class="stage">
    <section class="card card--front" aria-label="Card front">
      <h1 class="wordmark">VELMIRA CANDLES</h1>
      <div class="rule"></div>
      <p class="tagline">Hand-Poured Eco Soy Candles</p>
      <div class="person">
        <p class="person__name">LORRAINE QUIBELL</p>
        <p class="person__role">Founder</p>
      </div>
      <div class="contact">
        <p class="contact__phone">0438 276 904</p>
        <p class="contact__web">www.velmirawicks.com.au</p>
      </div>
    </section>
    <section class="card card--back" aria-label="Card back">
      <h2 class="wordmark">VELMIRA CANDLES</h2>
      <div class="rule"></div>
      <p class="tagline">Hand-Poured Eco Soy Candles</p>
    </section>
  </main>
</body>
</html>
```